Pinecrest Lockworks Business Card Design

Double Sided Business Card Design for a Locksmith company specializing in Safecracking, safe & vault service.

```html
<!DOCTYPE html>
<html lang="en">
<head>
<meta charset="utf-8">
<title>Pinecrest Lockworks – Business Card</title>
<link href="https://fonts.googleapis.com/css2?family=Roboto:wght@300;400;900&display=swap" rel="stylesheet">
<style>
  :root {
    --stage: #3b3b3b;
    --card: #1d1d1d;
    --green: #1f8a3b;
    --white: #ffffff;
    --muted: #d6d6d6;
    --ghost: #262626;
  }
  * { margin: 0; padding: 0; box-sizing: border-box; }
  html, body {
    width: 1200px; height: 900px; overflow: hidden;
    background: var(--stage);
    font-family: "Roboto", Arial, sans-serif;
  }
  .stage {
    width: 1200px; height: 900px;
    display: flex; flex-direction: column;
    align-items: center; justify-content: center; gap: 36px;
  }
  .card {
    width: 700px; height: 400px;
    background: var(--card);
    position: relative; overflow: hidden;
    box-shadow: 0 10px 30px rgba(0,0,0,.45);
  }
  /* front */
  .card-front { display: flex; align-items: center; justify-content: center; }
  .brand { display: flex; align-items: center; gap: 22px; }
  .brand-dot {
    width: 110px; height: 110px; border-radius: 50%;
    background: var(--green); flex: none;
  }
  .brand-name {
    font-weight: 900; color: var(--white);
    text-transform: uppercase; line-height: .95;
    font-size: 44px; letter-spacing: 1px;
  }
  /* back */
  .card-back { padding: 48px 0 0 56px; }
  .back-name {
    font-weight: 900; color: var(--white);
    text-transform: uppercase; line-height: .95;
    font-size: 26px; letter-spacing: .5px;
  }
  .holder { margin-top: 26px; }
  .holder-name { color: var(--green); font-size: 27px; font-weight: 400; }
  .holder-role { color: var(--muted); font-size: 17px; font-weight: 300; margin-top: 2px; }
  .address {
    margin-top: 22px; color: var(--muted);
    font-size: 17px; font-weight: 300; line-height: 1.3;
  }
  .contacts { list-style: none; margin-top: 18px; }
  .contacts li {
    display: flex; align-items: center; gap: 12px;
    color: var(--muted); font-size: 17px; font-weight: 300;
    line-height: 1.5;
  }
  .contacts svg { width: 14px; height: 14px; flex: none; }
  .ghost-mark {
    position: absolute; right: -60px; top: 80px;
    width: 380px; height: 380px; border-radius: 50%;
    background: var(--ghost);
  }
</style>
</head>
<body>
<main class="stage">
  <section class="card card-front" aria-label="Card front">
    <div class="brand">
      <span class="brand-dot"></span>
      <div class="brand-name">Pinecrest<br>Lockworks</div>
    </div>
  </section>

  <section class="card card-back" aria-label="Card back">
    <div class="ghost-mark"></div>
    <div class="back-name">Pinecrest<br>Lockworks</div>
    <div class="holder">
      <div class="holder-name">Marcus Hale</div>
      <div class="holder-role">Manager</div>
    </div>
    <div class="address">Your address, city<br>state, ZIP 0000</div>
    <ul class="contacts">
      <li>
        <svg viewBox="0 0 24 24" fill="none" stroke="var(--green)" stroke-width="2.2"><path d="M5 3h4l2 5-2.5 1.5a11 11 0 0 0 6 6L16 13l5 2v4a2 2 0 0 1-2 2A17 17 0 0 1 3 5a2 2 0 0 1 2-2z"/></svg>
        123-456-2100
      </li>
      <li>
        <svg viewBox="0 0 24 24" fill="none" stroke="var(--green)" stroke-width="2.2"><rect x="3" y="5" width="18" height="14" rx="1"/><path d="M3 6l9 7 9-7"/></svg>
        youremail@mailbox.com
      </li>
      <li>
        <svg viewBox="0 0 24 24" fill="none" stroke="var(--green)" stroke-width="2.2"><circle cx="12" cy="12" r="9"/><path d="M3 12h18M12 3c3 3 3 15 0 18M12 3c-3 3-3 15 0 18"/></svg>
        www.yourwebsite.com
      </li>
    </ul>
  </section>
</main>
</body>
</html>
```